Website - Tides Of Bloom

We are catalysts of change in people's lives.
We work with individuals and professionals to bring about instant substantial & transforming change in their lives.
We provide one-on-one lifestyle coaching by an experienced practitioner.
Our existing website is www.tidesofbloom.biz & this site contains our the basis for the content of our desired new project, so please examine this carefully.
We require a professional and captivating website that will instantly impress, engage invite our readers to click & invest their lives.
Our services do not come cheap, but are second to none.
Our website must be contemporary whilst reflecting indisputable class & ultra-confidence in the success of our work.
Target Market(s)
Those who seek to want to change in their lives. Those aged primarily between 30 and 50 years of age, male or female.
Industry/Entity Type
Work
Look and feel

```html
<!DOCTYPE html>
<html lang="en">
<head>
<meta charset="utf-8">
<title>Tides Of Bloom – Life Coaching</title>
<link href="https://fonts.googleapis.com/css2?family=Montserrat:wght@400;500;600;700&family=Open+Sans:wght@400;600&display=swap" rel="stylesheet">
<style>
:root{
  --black:#000;
  --ink:#1d1d1d;
  --text:#555;
  --orange:#e8772e;
  --orange-soft:rgba(232,119,46,.88);
  --teal:#2f8eab;
  --teal-dark:#1c6f8a;
  --amber:#ee8a1a;
  --amber-dark:#c9731a;
  --navy:#1d5572;
  --lime:#8cc63f;
  --sky:#5ab4cf;
  --grey-band:#f3f3f3;
  --footer:#2f2f2f;
  --footer-bottom:#1f1f1f;
  --footer-text:#d8d8d8;
}
*{margin:0;padding:0;box-sizing:border-box}
html,body{width:908px;height:1200px;overflow:hidden;background:#fff}
body{position:relative;font-family:"Montserrat",sans-serif;color:var(--ink)}
.site-header{position:absolute;left:0;top:0;width:908px;height:100px;background:var(--black)}
.brand{position:absolute;left:133px;top:18px;display:flex;align-items:center;gap:10px}
.brand-mark{width:40px;height:40px;border-radius:50%;background:var(--orange)}
.brand-name{font-weight:500;font-size:20px;color:#e6e6e6;line-height:1.05;width:90px}
.callout{position:absolute;right:132px;top:16px;display:flex;gap:6px;align-items:flex-start}
.callout-label{font-size:13px;color:#fff;display:block}
.callout-number{font-size:17px;font-weight:700;color:var(--orange);display:block;line-height:1.1}
.main-nav{position:absolute;right:132px;top:70px;display:flex;gap:25px;font-size:11px;color:#ddd}
.main-nav a{color:#ddd;text-decoration:none;position:relative}
.main-nav a.current{color:#fff;font-weight:600;font-size:11.5px}
.main-nav a.current::before{content:"";position:absolute;left:0;right:0;top:-11px;height:2px;background:var(--lime)}
.hero{position:absolute;left:0;top:100px;width:908px;height:418px;border-top:3px solid var(--sky);background:linear-gradient(100deg,#7c8b96 0%,#a9b7bf 25%,#d8dde0 48%,#9fb1ba 70%,#5f7684 100%)}
.hero-caption{position:absolute;left:133px;top:293px;width:370px;height:122px;background:var(--orange-soft);padding:14px 13px 0}
.hero-caption h1{font-size:28px;line-height:30px;font-weight:700;color:#fff;letter-spacing:.3px}
.hero-caption h1 em{font-family:Georgia,serif;font-weight:400;font-style:italic}
.hero-caption ul{list-style:none;margin-top:10px}
.hero-caption li{font-size:10.6px;color:#fff;line-height:16.5px;padding-left:11px;position:relative;white-space:nowrap;letter-spacing:-.2px}
.hero-caption li::before{content:"";position:absolute;left:0;top:7px;width:4px;height:4px;border-radius:50%;background:#2a9fc1}
.slider-dots{position:absolute;left:721px;top:399px;display:flex;gap:5px}
.slider-dots span{width:8px;height:8px;border-radius:50%;background:#e79c6a}
.slider-dots span.active{background:#fff}
.about{position:absolute;left:133px;top:543px;width:640px}
.about h2{font-size:22px;font-weight:700;color:var(--ink);letter-spacing:-.5px}
.about h2 span{color:var(--orange);font-size:17px;letter-spacing:-.3px}
.about .lead{font-size:10.5px;color:var(--ink);line-height:16px;margin-top:8px}
.about .body{font-size:10px;color:var(--text);line-height:16px}
.btn{display:inline-block;margin-top:12px;background:#3a3a3a;color:#fff;font-size:10.5px;padding:5px 8px;border:1px solid #222}
.cards{position:absolute;left:140px;top:698px;display:flex;gap:13px}
.card{width:203px;height:131px;position:relative;box-shadow:0 5px 5px -3px rgba(0,0,0,.2)}
.card-head{height:30px;padding:8px 13px;font-size:13px;font-weight:700;color:#fff}
.card-body{padding:11px 12px;font-size:9.2px;line-height:12.8px;color:#fff;letter-spacing:-.15px}
.card-body .more{display:block;margin-top:9px;font-weight:600;font-size:9.6px}
.card-arrow{position:absolute;right:-2px;top:-8px}
.card--business{background:var(--teal)}
.card--business .card-head{background:var(--teal-dark)}
.card--individual{background:var(--amber)}
.card--individual .card-head{background:var(--amber-dark)}
.card--video{background:var(--navy)}
.video-frame{position:absolute;left:0;top:30px;width:203px;height:101px;background:linear-gradient(90deg,#5b4a40,#8c7a6c 45%,#4b5564);display:flex;align-items:center;justify-content:center}
.play{width:44px;height:44px;border-radius:50%;background:#dfe4ee;border:3px solid #9ba6c4;display:flex;align-items:center;justify-content:center;padding-left:3px}
.testimonials{position:absolute;left:0;top:841px;width:908px;height:180px;background:var(--grey-band)}
.testimonials h2{position:absolute;left:133px;top:22px;font-size:23px;font-weight:700;color:var(--orange);letter-spacing:-.5px}
.quote{position:absolute;top:66px;width:292px;display:flex;gap:8px}
.quote--left{left:133px}
.quote--right{left:487px}
.avatar{width:69px;height:69px;flex:none;border-radius:50%;border:3px solid #bdbdbd;background:linear-gradient(160deg,#b9865f,#e8c8b0)}
.quote p{font-size:8.2px;line-height:11.8px;color:#666;margin-top:2px;letter-spacing:-.1px}
.quote cite{display:block;font-style:normal;font-size:9px;color:#222;margin-top:3px}
.divider{position:absolute;left:453px;top:66px;width:1px;height:70px;background:#ddd}
.site-footer{position:absolute;left:0;top:1026px;width:908px;height:146px;background:var(--footer);font-family:"Open Sans",sans-serif;color:var(--footer-text)}
.footer-col{position:absolute;top:24px;height:118px;border-right:1px solid #444}
.footer-col h3{font-family:"Montserrat",sans-serif;font-size:12px;font-weight:600;color:#fff;margin-bottom:10px}
.footer-col li{list-style:none;font-size:9px;line-height:17px}
.footer-col p{font-size:9px;line-height:14px}
.col-links{left:133px;width:92px}
.col-about{left:266px;width:127px}
.col-contact{left:431px;width:162px}
.follow{position:absolute;left:633px;top:40px;display:flex;gap:6px;align-items:center;font-family:"Montserrat",sans-serif;font-size:12px;font-weight:600;color:#fff}
.follow span.icon{width:15px;height:15px;border-radius:2px}
.footer-brand{position:absolute;left:670px;top:83px;display:flex;gap:8px;align-items:center;font-family:"Montserrat",sans-serif;font-size:15px;color:#9a9a9a;line-height:1;width:110px}
.footer-brand i{width:34px;height:34px;flex:none;border-radius:50%;background:#666}
.legal{position:absolute;left:0;top:1172px;width:908px;height:28px;background:var(--footer-bottom);font-family:"Open Sans",sans-serif;font-size:9px;color:#ccc;padding:7px 133px}
</style>
</head>
<body>
<header class="site-header">
  <div class="brand"><span class="brand-mark"></span><span class="brand-name">Tides Of Bloom</span></div>
  <div class="callout">
    <svg width="14" height="24" viewBox="0 0 14 24"><path d="M10 2 H6 C2 2 1 6 1 12 C1 18 2 22 6 22 H10 V17 H7 C6 15 6 9 7 7 H10 Z" fill="#888"/></svg>
    <div><span class="callout-label">If you want Change</span><span class="callout-number">+61 02 5550 1742</span></div>
  </div>
  <nav class="main-nav">
    <a class="current">Home</a><a>About us</a><a>Bussiness</a><a>Individual</a><a>Contact us</a>
  </nav>
</header>

<section class="hero" role="img" aria-label="Woman with arms raised in front of city towers">
  <div class="hero-caption">
    <h1>CHANGE <em>IS</em> YOURS</h1>
    <ul>
      <li>More choices about your behaviours and emotions</li>
      <li>Improve your relationships and the ways you communicate</li>
      <li>Create better results through becoming a greater thinker</li>
    </ul>
  </div>
  <div class="slider-dots"><span class="active"></span><span></span><span></span><span></span></div>
</section>

<section class="about">
  <h2>About <span>TIDES OF BLOOM</span></h2>
  <p class="lead">Not a lifelong project or years of therapy<br>Change begins today with our Master Practitioner</p>
  <p class="body">Join Mara Ellison, Tom Avery, Jo Halden, Rick Moreno, Sam Whitlow, Nina Carrow and hundreds of thousands of others who are achieving the life changing, consistent results you are dreaming of now.</p>
  <span class="btn">ReadMore</span>
</section>

<section class="cards">
  <article class="card card--business">
    <div class="card-head">BUSSINESS</div>
    <svg class="card-arrow" width="56" height="34" viewBox="0 0 56 34"><path transform="rotate(180 28 17)" d="M8 30 L24 14 L18 10 L50 2 L44 24 L38 18 L20 34 Z" fill="#5ab4cf"/></svg>
    <div class="card-body">Tides Of Bloom have worked with CEO's &amp; business owners throughout Australia, as catalysts to their outstanding success.<span class="more">Read More...</span></div>
  </article>
  <article class="card card--individual">
    <div class="card-head">INDIVIDUAL</div>
    <svg class="card-arrow" width="56" height="34" viewBox="0 0 56 34"><path transform="rotate(180 28 17)" d="M8 30 L24 14 L18 10 L50 2 L44 24 L38 18 L20 34 Z" fill="#f08a2a"/></svg>
    <div class="card-body">Mum's &amp; Dads experiencing marriage problems or who find themselves suddenly single, teenagers who have experienced death of someone close...<span class="more">Read More...</span></div>
  </article>
  <article class="card card--video">
    <div class="card-head">VIDEO</div>
    <svg class="card-arrow" width="56" height="34" viewBox="0 0 56 34"><path transform="rotate(180 28 17)" d="M8 30 L24 14 L18 10 L50 2 L44 24 L38 18 L20 34 Z" fill="#7cc242"/></svg>
    <div class="video-frame" role="img" aria-label="Video still of a television studio interview">
      <div class="play"><svg width="14" height="16" viewBox="0 0 14 16"><path d="M1 1 L13 8 L1 15 Z" fill="#111"/></svg></div>
    </div>
  </article>
</section>

<section class="testimonials">
  <h2>Testimonial</h2>
  <div class="quote quote--left">
    <div class="avatar" role="img" aria-label="Client portrait"></div>
    <div><p>"You are a legend. We have an audit in progress today and I was able to illustrate a "Live" recovery. Thank you for service above and beyond the call of duty. We really appreciate that."</p><cite>Coral Bay,</cite></div>
  </div>
  <div class="divider"></div>
  <div class="quote quote--right">
    <div class="avatar" role="img" aria-label="Client portrait"></div>
    <div><p>"You are a legend. We have an audit in progress today and I was able to illustrate a "Live" recovery. Thank you for service above and beyond the call of duty. We really appreciate that."</p><cite>Della Marsh,</cite></div>
  </div>
</section>

<footer class="site-footer">
  <div class="footer-col col-links"><h3>Links</h3><ul><li>Home</li><li>About us</li><li>Individual</li><li>Bussiness</li><li>Contact us</li></ul></div>
  <div class="footer-col col-about"><h3>About Us</h3><ul><li>FAQ</li><li>Member Benefits</li><li>Privacy Policy</li><li>Site Map</li></ul></div>
  <div class="footer-col col-contact"><h3>Contact us</h3><p>Call Us: +61 02 5550 1742<br>Email: hello@tidesofbloom.biz</p></div>
  <div class="follow">Follow Us:
    <span class="icon" style="background:#3b5998"></span><span class="icon" style="background:#2aa3ef"></span><span class="icon" style="background:#cb2027"></span><span class="icon" style="background:#dd4b39"></span>
  </div>
  <div class="footer-brand"><i></i>Tides Of Bloom</div>
</footer>
<div class="legal">© copyright 2013 Tides Of Bloom. All right Reserved.</div>
</body>
</html>
```